KTW Business cards & stationary
Business cards and stationary
KTW Business cards & stationary - Real Estate
Creative Brief
Use same font as used in my logo
Im not sure if my logo font will look good
Professional
Darnell Wisecamp
President
42 Tarrow Lane Suite 514 East Orange, NJ 07018
Darnell@kelvatrowrealty.example
KelvatrowRealty.example
company name on business card
loriswex loriswex
i definitely want to promote the website address on the card in a classy way also the company name should appear along with logo on the front

```html
<!DOCTYPE html>
<html lang="en">
<head>
<meta charset="utf-8">
<title>KTW Realty Corp. Letterhead</title>
<link href="https://fonts.googleapis.com/css2?family=Cinzel:wght@500&family=Open+Sans:ital,wght@0,400;0,700;1,700&display=swap" rel="stylesheet">
<style>
  :root {
    --backdrop: #1f1f1f;
    --paper: #ffffff;
    --paper-shade: #efefef;
    --brand-blue: #0b5fb8;
    --band-blue-deep: #0a57c2;
    --band-blue-light: #0878b5;
    --swoosh-grey: #8a8c90;
    --faint-mark: #eef1f4;
    --white: #ffffff;
  }
  html, body {
    margin: 0;
    width: 930px;
    height: 1200px;
    overflow: hidden;
    background: var(--backdrop);
  }
  .letterhead {
    position: absolute;
    left: 58px;
    top: 75px;
    width: 815px;
    height: 1052px;
    background: radial-gradient(ellipse at 50% 45%, var(--paper) 55%, var(--paper-shade) 100%);
    overflow: hidden;
    font-family: "Open Sans", Arial, sans-serif;
  }
  .brand {
    position: absolute;
    top: 40px;
    left: 0;
    width: 100%;
    text-align: center;
  }
  .brand-square {
    display: block;
    width: 72px;
    height: 72px;
    margin: 0 auto 28px;
    background: var(--brand-blue);
    border-radius: 8px;
  }
  .brand-name {
    margin: 0;
    font-family: "Cinzel", Georgia, serif;
    font-weight: 500;
    font-size: 34px;
    line-height: 1;
    letter-spacing: 1px;
    color: var(--brand-blue);
  }
  .faint-mark {
    position: absolute;
    top: 430px;
    left: 0;
    width: 100%;
    text-align: center;
    font-family: "Cinzel", Georgia, serif;
    font-weight: 500;
    font-size: 200px;
    line-height: 1;
    color: var(--faint-mark);
  }
  .footer-band {
    position: absolute;
    left: 0;
    bottom: 0;
    width: 815px;
    height: 133px;
    display: block;
  }
  .website {
    position: absolute;
    left: 26px;
    bottom: 16px;
    margin: 0;
    font-size: 18px;
    font-weight: 700;
    font-style: italic;
    color: var(--white);
  }
  .contact {
    position: absolute;
    right: 25px;
    bottom: 14px;
    margin: 0;
    text-align: right;
    font-size: 12.5px;
    line-height: 17px;
    color: var(--white);
  }
  .contact b { font-weight: 700; }
</style>
</head>
<body>
  <main class="letterhead">
    <header class="brand">
      <span class="brand-square"></span>
      <h1 class="brand-name">KTW Realty Corp.</h1>
    </header>

    <div class="faint-mark" aria-hidden="true">KTW</div>

    <svg class="footer-band" viewBox="0 0 815 133" preserveAspectRatio="none" aria-hidden="true">
      <defs>
        <linearGradient id="bandGradient" x1="0" y1="0" x2="1" y2="0">
          <stop offset="0" stop-color="var(--band-blue-deep)"/>
          <stop offset="0.55" stop-color="var(--band-blue-light)"/>
          <stop offset="1" stop-color="var(--band-blue-deep)"/>
        </linearGradient>
      </defs>
      <path d="M0,16 C200,82 420,100 570,72 C690,50 765,26 815,24 L815,133 L0,133 Z" fill="url(#bandGradient)"/>
      <path d="M0,2 C200,70 420,90 570,60 C690,36 765,14 815,10 L815,18 C765,20 690,44 570,68 C420,96 200,78 0,10 Z" fill="var(--swoosh-grey)"/>
    </svg>

    <p class="website">www.KelvatrowRealty.example</p>
    <p class="contact">
      <b>P:</b> 973-555-0142 <b>M:</b> 973-555-0187<br>
      <b>F:</b> 973-555-0163&nbsp; <b>E:</b> Darnell@kelvatrowrealty.example<br>
      42 Tarrow Lane, Ste. 514, East Orange, NJ 07018
    </p>
  </main>
</body>
</html>
```